Progressive Metal Band Looking for Unique New Album Cover

We are a progressive/thrash metal band called Velvet Hollow and are looking for a thought provoking design for our upcoming album "A spark to Transcend" which when broken down means to us "A tick" is a moment in the past that feels like it's moved by very fast and "Ameliorate" to improve or make something better.

This album is a collection of some of our older songs that haven't been released yet so the theme that we want this cover to represent is progression itself (our personal progression). Though we are a metal band and like to use some graphic imagery we like to try and distance ourselves from the typical demons and skulls. The style of the design that we're looking for would be something painted or hand drawn, something that looks natural or at least not so computer generated. An idea for how we want the album to be presented we were thinking one way that we could have a visual representation of progression would be a clarity gradient from left to right. Have the detail of the design become more sharp and detailed but we are open to changes as well as letting creative liberties being taken in order to allow the best possible product to be made.

We want this design to cover the front and back of the package so the design in mind would need to fill a 5x10 digipak. I've also attached demo's of two songs that will appear on this album as well as some imagery that we've associated ourselves with in the past. We do have a logo that due to its size could not be uploaded here, once the final design is chosen we would like to have it added to the design (the logo in the images provided is the logo that will be used).

The track list for the album is:
1. Grimwake
2. Mechanized Bondage
3. Storm of Spite
4. Rivers of Dust
5. Pancake Outlaw

Target Market(s)

Metal, Progressive Metal, Thrash Metal, Hard Rock

Industry/Entity Type

Progressive

Requirements
Should not have
• Clocks, hourglasses, bugs, cocoons

```html
<!DOCTYPE html>
<html lang="en">
<head>
<meta charset="utf-8">
<title>A spark to Transcend — Velvet Hollow digipak</title>
<link rel="stylesheet" href="https://fonts.googleapis.com/css2?family=Jim+Nightshade&display=swap">
<style>
  :root {
    --stage: #5f4c47;
    --panel-black: #050404;
    --ember: #d08466;
    --coral: #b9615a;
    --amber: #c07a3c;
    --rust: #8e4540;
    --smoke: #5a4a4c;
    --mauve: #7c6068;
    --crimson: #b8484a;
    --blood: #7a2a2c;
    --moss: #1e3a2a;
    --shadow-grey: #2a2428;
    --ink-white: #f4efe8;
  }
  * { box-sizing: border-box; margin: 0; padding: 0; }
  html, body {
    width: 1200px;
    height: 900px;
    overflow: hidden;
    background: var(--stage);
  }
  .digipak {
    position: absolute;
    left: 98px;
    top: 199px;
    width: 982px;
    height: 491px;
    display: flex;
    box-shadow: 2px 3px 6px rgba(0, 0, 0, 0.45);
  }
  .panel {
    position: relative;
    width: 491px;
    height: 491px;
    overflow: hidden;
    background: var(--panel-black);
  }
  .artwork {
    position: absolute;
    inset: 0;
  }
  /* Back cover: softer, hazier tones — the starting point of the clarity gradient */
  .back-cover .artwork {
    background:
      radial-gradient(ellipse 34% 14% at 26% 30%, var(--ember) 0%, rgba(208,132,102,0.85) 55%, transparent 100%),
      radial-gradient(ellipse 26% 16% at 60% 26%, var(--amber) 0%, rgba(192,122,60,0.7) 50%, transparent 100%),
      radial-gradient(ellipse 40% 11% at 50% 20%, rgba(185,97,90,0.8) 0%, transparent 100%),
      radial-gradient(ellipse 22% 26% at 88% 16%, var(--mauve) 0%, rgba(124,96,104,0.5) 55%, transparent 100%),
      radial-gradient(ellipse 20% 18% at 52% 66%, var(--coral) 0%, rgba(185,97,90,0.7) 55%, transparent 100%),
      radial-gradient(ellipse 48% 10% at 50% 76%, var(--rust) 0%, rgba(142,69,64,0.6) 55%, transparent 100%),
      radial-gradient(ellipse 30% 24% at 92% 70%, var(--smoke) 0%, transparent 100%),
      radial-gradient(ellipse 20% 14% at 8% 8%, var(--smoke) 0%, transparent 100%),
      var(--panel-black);
  }
  /* Front cover: crisper edges — the sharp end of the clarity gradient */
  .front-cover .artwork {
    background:
      radial-gradient(circle at 50% 52%, var(--crimson) 0 9%, var(--blood) 9% 13%, var(--moss) 13% 20%, var(--blood) 20% 24%, var(--crimson) 24% 31%, var(--moss) 31% 35%, var(--panel-black) 35% 40%, var(--shadow-grey) 40% 46%, var(--panel-black) 46% 52%, var(--shadow-grey) 52% 58%, var(--panel-black) 58% 66%, rgba(42,36,40,0.8) 66% 72%, var(--panel-black) 72%);
  }
  .track-list {
    position: absolute;
    left: 22px;
    top: 326px;
    list-style: none;
    font-family: "Jim Nightshade", cursive;
    font-size: 19px;
    line-height: 28px;
    letter-spacing: 1px;
    color: var(--ink-white);
    text-shadow: 1px 1px 2px rgba(0, 0, 0, 0.9);
  }
  .album-title {
    position: absolute;
    left: 0;
    right: 0;
    top: 430px;
    text-align: center;
    font-family: "Jim Nightshade", cursive;
    font-weight: 400;
    font-size: 32px;
    letter-spacing: 9px;
    color: var(--ink-white);
  }
</style>
</head>
<body>
  <main class="digipak">
    <section class="panel back-cover">
      <div class="artwork" role="img" aria-label="Hand-drawn woodcut-style illustration of long flowing hair with faces in ember, coral and rust tones on black, softer in focus"></div>
      <ol class="track-list">
        <li>1. Grimwake</li>
        <li>2. Mechanized Bondage</li>
        <li>3. Storm of Spite</li>
        <li>4. Rivers of Dust</li>
        <li>5. Pancake Outlaw</li>
      </ol>
    </section>
    <section class="panel front-cover">
      <div class="artwork" role="img" aria-label="Sharply detailed hand-drawn radial illustration of a figure with outstretched arms inside a ring of crimson flowing hair and faces over dark green and black"></div>
      <h1 class="album-title">A spark to Transcend</h1>
    </section>
  </main>
</body>
</html>
```